HollowPine Ventures Inc. Business Card Design

My business is custom renovations and homes.I would need to have a new business logo created to go along with my company name. The business card should be of a modern style as this is the market I am focused on. I would need my contact information and website posted on the card. I would also like to list a few of the tasks I conduct on the card (such as: Renovations, Additions, Repairs, New Homes, Design, Consultations). On the reverse of the card I currently have just my logo and my motto, "Shaping A Bold Path". However, I am open to completely changing everything as I am starting a new year and would like to excel further. Any new ideas and suggestions are always welcomed. Thank you.

Target Market(s)

Upscale residential and commercial renovations and builds

Industry/Entity Type

Business

Contact Information for Business Card

I would like the design to be able to be laser cut or burnt onto a wooden business card. I will be creating one option of cards for really loyal customers (wooden) and a second option for the everyday customer (paper).

Font styles to use
Other font styles liked:
• Calibri / anything of mordern taste

Colors
f37122
5c5c5c
474747
ffffff

Requirements
Must have
• I would like the colours of my business to be a sharp orange and grey. I believe this will symbolize a modern style. I am open to other suggestions if this is not suitable for the designers tastes. My contact info as follows:
• Will Marsh
• President
• HollowPine Ventures Inc.
• 555-214-3987
• will@hollowpineventures.example
• I would like my website (currently under construction) hollowpineventures.example on the card aswell.
Nice to have
• Along with a modern logo representing HollowPine, I would like something on the card besides the logo and contact information. Perhaps a small background design. I feel it may be nice to have my services listed on the card (in smaller font on the bottom) Renovations, Additions, Repairs, Design, Consultations.
Should not have
• The business card should not have too many different colors. Should not have rounded corners.

```html
<!DOCTYPE html>
<html lang="en">
<head>
<meta charset="utf-8">
<title>HollowPine Ventures Inc. – Business Card</title>
<link href="https://fonts.googleapis.com/css2?family=Roboto:wght@400;500;700&display=swap" rel="stylesheet">
<style>
  :root {
    --orange: #f37122;
    --card: #2a2a2c;
    --stripe-grey: #5c5c5c;
    --backdrop: #474747;
    --white: #ffffff;
    --text-soft: #e6e6e6;
  }
  * { margin: 0; padding: 0; box-sizing: border-box; }
  html, body {
    width: 1200px; height: 576px; overflow: hidden;
    background: var(--backdrop);
    font-family: "Roboto", Arial, sans-serif;
  }
  .canvas { position: relative; width: 1200px; height: 576px; }
  .card {
    position: absolute; top: 138px;
    width: 484px; height: 294px;
    background: var(--card);
  }
  .card--back { left: 82px; }
  .card--front { left: 602px; }

  /* Back */
  .back-name {
    position: absolute; left: 0; right: 0; top: 112px;
    text-align: center;
    font-size: 44px; font-weight: 700; color: var(--orange);
    letter-spacing: 0.5px;
  }
  .services {
    position: absolute; left: 0; right: 0; top: 262px;
    text-align: center;
    font-size: 13px; color: var(--text-soft);
  }
  .services .sep { color: var(--orange); margin: 0 3px; }

  /* Front */
  .band {
    position: absolute; left: 0; top: 0; bottom: 0; width: 41px;
    background: var(--orange);
  }
  .band-edge {
    position: absolute; left: 41px; top: 0; bottom: 0; width: 5px;
    background: var(--stripe-grey);
  }
  .company { position: absolute; left: 67px; top: 24px; }
  .company-name {
    font-size: 25px; font-weight: 700; color: var(--white); line-height: 1;
  }
  .company-suffix {
    font-size: 17px; color: var(--text-soft); margin-top: 3px; line-height: 1;
  }
  .mark {
    position: absolute; right: 34px; top: 28px;
    width: 44px; height: 44px; background: var(--orange);
  }
  .person { position: absolute; left: 67px; top: 166px; }
  .person-name {
    font-size: 20px; font-weight: 700; color: var(--orange);
    letter-spacing: 1px; line-height: 1;
  }
  .person-role {
    font-size: 12px; color: var(--white); margin-top: 7px;
  }
  .contacts {
    position: absolute; left: 67px; top: 216px;
    list-style: none;
  }
  .contacts li {
    display: flex; align-items: center;
    height: 17.5px;
    font-size: 13px; color: var(--text-soft);
  }
  .contacts svg { width: 11px; height: 11px; margin-right: 13px; fill: var(--orange); }
  .contacts .accent { color: var(--orange); }
</style>
</head>
<body>
<div class="canvas">
  <section class="card card--back">
    <div class="back-name">HollowPine</div>
    <p class="services">
      Renovations<span class="sep">|</span>Additions<span class="sep">|</span>Repairs<span class="sep">|</span>Design<span class="sep">|</span>Consultations
    </p>
  </section>

  <section class="card card--front">
    <div class="band"></div>
    <div class="band-edge"></div>
    <div class="company">
      <div class="company-name">HollowPine</div>
      <div class="company-suffix">Ventures Inc.</div>
    </div>
    <div class="mark"></div>

    <div class="person">
      <div class="person-name">Will Marsh</div>
      <div class="person-role">President</div>
    </div>

    <ul class="contacts">
      <li>
        <svg viewBox="0 0 12 12" aria-hidden="true"><path d="M1 3.5C1 2 3 1 6 1s5 1 5 2.5v1H8.5V3.5h-5v1H1z M2.5 6h7l1 5h-9z M6 7a1.2 1.2 0 1 0 0 2.4A1.2 1.2 0 0 0 6 7z"/></svg>
        555-214-3987
      </li>
      <li>
        <svg viewBox="0 0 12 12" aria-hidden="true"><path d="M0.5 2h11v8h-11z M1.5 3l4.5 3.5L10.5 3" fill="none" stroke="#f37122" stroke-width="1.2"/><rect x="0.5" y="2" width="11" height="8" fill="#f37122"/><path d="M1 2.6l5 3.6 5-3.6" fill="none" stroke="#2a2a2c" stroke-width="1"/></svg>
        will@hollowpineventures.example
      </li>
      <li>
        <svg viewBox="0 0 12 12" aria-hidden="true"><circle cx="6" cy="6" r="5"/><path d="M1 6h10M6 1v10M6 1c-2.5 2.5-2.5 7.5 0 10M6 1c2.5 2.5 2.5 7.5 0 10" fill="none" stroke="#2a2a2c" stroke-width="0.8"/></svg>
        www.<span class="accent">hollowpineventures</span>.example
      </li>
    </ul>
  </section>
</div>
</body>
</html>
```